Business card design needed

This is a roofing company that specialises in metal roofs on period homes. I want to market to the more affluent areas in Melbourne as they are very expensive homes and period style. If you look at period homes in Melbourne you will see the metal roofs with ornate guttering and lattice work. An image of a roof or part of it would look good on the card - as it will catch the eye of the home owner in my view.

I dont have a logo so feel free to do what you want. I am open to all ideas and will choose the most appropriate.

I want to make the card look very professional and upmarket. Most roofers just use cards made cheaply, so this is my opportunity to differentiate from those. I dont want a cheap looking card. Must really look professional and make the home owner think I am very good at what I do.

I am going to put these cards in letter boxes to market my business. As this has worked before.

A good example of period homes with the roofs I work on are:
http://www.tindlebrookhouses.com.au/Tindlebrook-Houses-photo-gallery.html
Please check out the houses in the gallery. If I can get the message across with a beautiful photo of a roof - the home owner will be enticed to call me based on the image. I believe the image of the period home roof - or part of - will make a difference. As most of my competitors just have a sketch or words.

I will be making a quality card that is thick and printed in high resolution.

Target Market(s)

Home owners who are most likely tertiary educated and high income earners.

Industry/Entity Type

Roofing

Contact Information for Business Card

Mr Dean Pellowe
Professional Roofing Expert (est 30 years)
No obligation appraisal
Licensed. Quality. Guaranteed.

Mobile: 0438 726 913
Fax: 9587 3046
Email: crestlinetiles.vic@quillmail.com

On the back of the card can you put.....
Metal Roofing Specialists
Quality Period Home Experience
New and Old Roofing Expertise
Roof Maintenance and Repair
Over 30 years experience
References Provided
Polite and Punctual

Requirements
Nice to have
• I am open to all ideas. Layout and design is up to you. Go for it.

```html
<!DOCTYPE html>
<html lang="en">
<head>
<meta charset="utf-8">
<title>Dean Pellowe – Roofing Business Card</title>
<link rel="stylesheet" href="https://fonts.googleapis.com/css2?family=Arimo:wght@400;700&display=swap">
<style>
  :root {
    --roof-blue: #0590d9;
    --ink: #0b0b0b;
    --paper: #ffffff;
    --frame: #8a8a8a;
    --card-edge: #555555;
  }
  html, body {
    margin: 0;
    padding: 0;
    width: 1200px;
    height: 745px;
    overflow: hidden;
    background: var(--paper);
  }
  .sheet {
    display: block;
    width: 1200px;
    height: 745px;
    font-family: "Arimo", Arial, sans-serif;
  }
  .sheet-frame { fill: none; stroke: var(--frame); stroke-width: 1.5; }
  .card-edge { fill: var(--paper); stroke: var(--card-edge); stroke-width: 1; }
  .fill-blue { fill: var(--roof-blue); }
  .fill-ink { fill: var(--ink); }
  .fill-paper { fill: var(--paper); }

  .owner-name { fill: var(--roof-blue); font-weight: 700; font-size: 20px; }
  .tagline { fill: var(--paper); font-size: 12.5px; }
  .tagline-strong { fill: var(--paper); font-size: 12.5px; font-weight: 700; text-decoration: underline; }
  .contact-label { fill: var(--paper); font-weight: 700; font-size: 17px; }
  .contact-value { fill: var(--roof-blue); font-weight: 700; font-size: 17px; }
  .email-label { fill: var(--paper); font-weight: 700; font-size: 11px; }
  .email-value { fill: var(--roof-blue); font-weight: 700; font-size: 11px; }

  .service-list {
    fill: var(--roof-blue);
    stroke: var(--ink);
    stroke-width: 1.6px;
    paint-order: stroke fill;
    font-weight: 700;
    font-size: 15px;
    text-anchor: middle;
  }
  .back-name { fill: var(--ink); font-weight: 700; font-size: 24px; }
</style>
</head>
<body>
<svg class="sheet" viewBox="0 0 1200 745" xmlns="http://www.w3.org/2000/svg">
  <rect class="sheet-frame" x="1" y="1" width="1196" height="741"/>

  <!-- Front of card (portrait) -->
  <g class="card-front">
    <rect class="card-edge" x="110.5" y="51.5" width="342" height="584"/>

    <!-- vertical bars -->
    <rect class="fill-ink" x="155" y="160" width="21" height="212"/>
    <rect class="fill-ink" x="179" y="160" width="19" height="168"/>
    <rect class="fill-ink" x="205" y="160" width="20" height="245"/>
    <rect class="fill-ink" x="231" y="250" width="20" height="108"/>

    <!-- title panel -->
    <path class="fill-ink" d="M182 77 H452 V167 H182 Q168 167 168 153 V91 Q168 77 182 77 Z"/>
    <polygon class="fill-blue" points="148,71 231,71 162,114"/>

    <text class="owner-name" x="443" y="106" text-anchor="end">Mr.Dean Pellowe</text>
    <text class="tagline" x="443" y="127" text-anchor="end">Professional Roofing Expert (est 30 years)</text>
    <text class="tagline" x="443" y="142" text-anchor="end">No obligation appraisal Licensed.</text>
    <text class="tagline-strong" x="443" y="158" text-anchor="end">Quality Guaranteed</text>

    <!-- contact panel -->
    <path class="fill-ink" d="M110 185 H385 Q405 185 405 205 V243 Q405 263 385 263 H110 Z"/>
    <polygon class="fill-blue" points="340,180 417,177 405,221"/>

    <!-- phone icon -->
    <path class="fill-blue" d="M128 203 l3 -1 2 5 -2 2 q1 3 4 5 l2 -2 5 2 -1 3 q-2 2 -5 1 q-7 -3 -9 -10 q-1 -3 1 -5 z"/>
    <text class="contact-label" x="145" y="216">Mobile:</text>
    <text class="contact-value" x="216" y="216">0438 726 913</text>

    <!-- fax icon -->
    <g class="fax-icon">
      <rect class="fill-paper" x="129" y="220" width="10" height="5"/>
      <rect class="fill-paper" x="126" y="226" width="16" height="7" rx="1"/>
    </g>
    <text class="contact-label" x="175" y="232">Fax:</text>
    <text class="contact-value" x="216" y="232">9587 3046</text>

    <!-- mail icon -->
    <g class="mail-icon">
      <rect class="fill-paper" x="122" y="237" width="24" height="10"/>
      <polyline points="122,237 134,244 146,237" fill="none" stroke="#0b0b0b" stroke-width="1.2"/>
    </g>
    <text class="email-label" x="175" y="246">Email:</text>
    <text class="email-value" x="216" y="246" textLength="188" lengthAdjust="spacingAndGlyphs">crestlinetiles.vic@quillmail.com</text>

    <!-- lower shards -->
    <polygon class="fill-ink" points="110,475 110,493 330,612 346,612"/>
    <polygon class="fill-blue" points="130,453 338,443 315,563"/>
    <polygon class="fill-blue" points="110,498 110,635 337,632"/>
  </g>

  <!-- Back of card (landscape) -->
  <g class="card-back">
    <rect class="card-edge" x="500.5" y="148.5" width="584" height="341"/>
    <polygon class="fill-ink" points="1046,477 1058,423 1065,487"/>
    <polygon class="fill-blue" points="501,149 1084,149 1084,328 1048,475 501,378"/>

    <text class="service-list" x="810" y="222">Metal Roofing Specialists</text>
    <text class="service-list" x="810" y="241">Quality Period  Home Experience</text>
    <text class="service-list" x="810" y="260">New and Old Roofing Expertise Roof</text>
    <text class="service-list" x="810" y="279">Maintenance and Repair Over 30 years experience</text>
    <text class="service-list" x="810" y="298">References Provided Polite and Punctual</text>

    <text class="back-name" x="512" y="477">Mr.Dean Pellowe</text>
  </g>
</svg>
</body>
</html>
```